Flyer for a marketing

We are a holistic mental health facility in need of a flyer to help promote our services and encourage more people to seek care. See the attachment to tell you more. We prefer warm green colors or rich blue. Thank you.

```html
<!DOCTYPE html>
<html lang="en">
<head>
<meta charset="utf-8">
<title>Evergreen Mind Health and Wellness — Flyer</title>
<link href="https://fonts.googleapis.com/css2?family=Roboto+Slab:wght@700&family=Montserrat:wght@300;800&family=Nunito+Sans:wght@400;600;700;800&display=swap" rel="stylesheet">
<style>
  :root {
    --backdrop: #5e5e5e;
    --paper: #f7f7f5;
    --navy: #1d3f7a;
    --ink-navy: #14306a;
    --sky: #3fb8e8;
    --leaf: #5a9a3f;
    --leaf-deep: #4f8c37;
    --footer-blue: #2a5591;
    --white: #ffffff;
    --body-ink: #2c3a55;
  }
  * { box-sizing: border-box; margin: 0; padding: 0; }
  html, body { width: 1200px; height: 900px; overflow: hidden; }
  body {
    background: var(--backdrop);
    display: flex; align-items: center; justify-content: center;
    font-family: "Nunito Sans", Arial, sans-serif;
  }
  .flyer {
    position: relative;
    width: 600px; height: 850px;
    background: var(--paper);
    overflow: hidden;
    display: flex; flex-direction: column;
  }
  .hero {
    position: relative;
    flex: none;
    height: 370px;
    overflow: hidden;
    background: linear-gradient(180deg, #fbfbfa 0%, #f1f1ef 32%, #c9cbc3 48%, #8c9a82 60%, #a7aca6 78%, #d7d4cf 100%);
  }
  .hero-photo {
    position: absolute; left: 0; bottom: 0; width: 290px; height: 230px;
    background: radial-gradient(ellipse at 50% 60%, #b98463 0%, #7b4e36 38%, #3a2418 70%, rgba(214,200,180,0.6) 100%);
  }
  .brand {
    position: absolute; top: 32px; right: 36px;
    display: flex; flex-direction: column; align-items: flex-end;
  }
  .brand-lockup { display: flex; align-items: center; gap: 14px; }
  .brand-dot { width: 46px; height: 46px; border-radius: 50%; background: var(--sky); }
  .brand-name {
    font-family: "Nunito Sans", Arial, sans-serif; font-weight: 700;
    color: var(--ink-navy); font-size: 17px; line-height: 1.05;
    border-left: 2px solid var(--ink-navy); padding-left: 12px;
  }
  .brand-tagline {
    margin-top: 10px;
    font-family: "Montserrat", Arial, sans-serif; font-weight: 300;
    color: var(--navy); font-size: 15px; letter-spacing: 0.5px;
  }
  .headline {
    position: absolute; right: 36px; top: 205px;
    font-family: "Roboto Slab", Georgia, serif; font-weight: 700;
    color: var(--white); font-size: 42px; line-height: 1.1; text-align: right;
    text-shadow: 0 1px 4px rgba(0,0,0,0.25);
  }
  .intro {
    flex: none;
    background: linear-gradient(90deg, var(--leaf-deep), var(--leaf));
    color: var(--white); text-align: center;
    padding: 24px 40px 26px;
    font-size: 16px; line-height: 1.35; font-weight: 600;
  }
  .intro p + p { margin-top: 14px; font-weight: 700; }
  .why {
    flex: none;
    background: var(--paper); text-align: center;
    padding: 18px 40px 20px; color: var(--body-ink);
    font-size: 15px; line-height: 1.32;
  }
  .why h2 {
    font-family: "Montserrat", Arial, sans-serif; font-weight: 800;
    color: var(--navy); font-size: 24px; margin-bottom: 8px;
  }
  .contact {
    flex: 1; background: var(--footer-blue); color: var(--white);
    padding: 18px 36px; font-size: 14px;
  }
  .contact-name {
    font-family: "Montserrat", Arial, sans-serif; font-weight: 800;
    color: var(--sky); font-size: 16px; margin-bottom: 8px;
  }
  .contact-grid { display: grid; grid-template-columns: 1fr 1fr; gap: 6px 18px; }
  .contact-item { display: flex; align-items: center; gap: 8px; }
  .contact-item.wide { grid-column: 1 / 3; }
  .contact-icon { width: 18px; height: 18px; flex: none; }
</style>
</head>
<body>
  <main class="flyer">
    <section class="hero">
      <div class="hero-photo" role="img" aria-label="Photo of a smiling young woman with curly hair outdoors in warm sunlight"></div>
      <div class="brand">
        <div class="brand-lockup">
          <span class="brand-dot"></span>
          <span class="brand-name">Evergreen<br>Mind<br>Health<br>and<br>Wellness</span>
        </div>
        <span class="brand-tagline">The Care You Deserve</span>
      </div>
      <h1 class="headline">The Care You<br>Deserve</h1>
    </section>

    <section class="intro">
      <p>Evergreen Mind Health and Wellness,<br>where deserving patients meet compassionate providers.</p>
      <p>We are accepting new patients, no waiting list.<br>Your mental health matters, so make it a priority and<br>call us today for an appointment.</p>
    </section>

    <section class="why">
      <h2>WHY CHOOSE US?</h2>
      <p>We are an integrative holistic psychiatric center.<br>
      Our mission is to provide compassionate quality care.<br>
      We provide psychiatric services including medication<br>
      management and psychotherapy.<br>
      We listen, care, and empower you to live better.<br>
      We accept major insurances.</p>
    </section>

    <footer class="contact">
      <div class="contact-name">EVERGREEN MIND HEALTH AND WELLNESS, APNC</div>
      <div class="contact-grid">
        <div class="contact-item wide">
          <svg class="contact-icon" viewBox="0 0 18 18"><circle cx="9" cy="9" r="9" fill="#3fb8e8"/><path d="M9 4a3 3 0 0 0-3 3c0 2.3 3 6 3 6s3-3.7 3-6a3 3 0 0 0-3-3z" fill="#2a5591"/><circle cx="9" cy="7" r="1" fill="#3fb8e8"/></svg>
          1480 Maple Ridge Road, Suite 210 Oakdale, CA 95361
        </div>
        <div class="contact-item">
          <svg class="contact-icon" viewBox="0 0 18 18"><circle cx="9" cy="9" r="9" fill="#3fb8e8"/><path d="M6 4.5l1.6 2.2-1 1.1a6 6 0 0 0 3.6 3.6l1.1-1 2.2 1.6-.9 1.6c-4 .2-7.6-3.4-7.4-7.4z" fill="#2a5591"/></svg>
          (555) 214-6730
        </div>
        <div class="contact-item">
          <svg class="contact-icon" viewBox="0 0 18 18"><circle cx="9" cy="9" r="9" fill="#3fb8e8"/><rect x="4.5" y="6" width="9" height="6.5" fill="#2a5591"/><path d="M4.5 6l4.5 3.5L13.5 6" stroke="#3fb8e8" fill="none"/></svg>
          hello@evergreenmindhealth.com
        </div>
        <div class="contact-item">
          <svg class="contact-icon" viewBox="0 0 18 18"><circle cx="9" cy="9" r="9" fill="#3fb8e8"/><rect x="5" y="7" width="8" height="6" fill="#2a5591"/><rect x="6.5" y="4.5" width="5" height="3" fill="#2a5591"/></svg>
          (555) 318-4092
        </div>
        <div class="contact-item">
          <svg class="contact-icon" viewBox="0 0 18 18"><circle cx="9" cy="9" r="9" fill="#3fb8e8"/><circle cx="9" cy="9" r="4.5" fill="none" stroke="#2a5591" stroke-width="1.3"/><path d="M4.5 9h9M9 4.5c-2 2.5-2 6.5 0 9M9 4.5c2 2.5 2 6.5 0 9" stroke="#2a5591" fill="none" stroke-width="1"/></svg>
          evergreenmindhealth.com
        </div>
      </div>
    </footer>
  </main>
</body>
</html>
```